Single Page Timetracking Dashboard Desktop App UI Design (Figma Link required)

Main Idea: a SaaS tool where employees can add their time and project in a playful way. There is a infographics and a list with tasks as well.

Based on the attached concept.png the brief is following:

- check the attached rough scribble
- add own ideas or change things if they add value
- Style: colourful, nerdy, professional saas, modern, beautiful, white space
- Quality expectation: inspiration1+2.png
- I will need a Figma link
- desktop only
- make something fresh and unique

Process:
I need to include 2-3 feedback rounds that will span probably around 7 days

Target Market(s)

Internal Business Tool for a Software Development Company

Industry/Entity Type

IT

Other font styles liked:
• Could be monospace, not a must though

Requirements
Must have
• At least one page; Figma Link to the design;
Nice to have
• Microinterations like drop-down, hover/active colors; functionality specifications
Should not have
• Mobile view

```html
<!DOCTYPE html>
<html lang="en">
<head>
<meta charset="utf-8">
<title>Timetracking Dashboard</title>
<link href="https://fonts.googleapis.com/css2?family=Inter:wght@400;500;600;700&display=swap" rel="stylesheet">
<style>
:root{
  --backdrop:#bdbdbd;
  --coral:#ff8a85;
  --coral-strong:#ff6e6c;
  --coral-soft:#ffe3e3;
  --cream:#fff4ec;
  --orange:#f9a94b;
  --ink:#2d2a2b;
  --panel:#3a3335;
  --panel-head:#433c3e;
  --muted:#8a8a8a;
  --line:#eeeeee;
  --row:#f7f7fa;
  --green:#6ee35c;
  --blue:#8fd1f7;
  --pink:#ffc9cf;
  --yellow:#f7e44a;
  --white:#ffffff;
}
*{box-sizing:border-box;margin:0;padding:0}
html,body{width:1200px;height:867px;overflow:hidden}
body{background:var(--backdrop);font-family:"Inter",sans-serif;color:var(--ink);position:relative}
.dashboard{position:absolute;left:311px;top:33px;width:1015px;height:1512px;transform:scale(.529);transform-origin:0 0;background:var(--white);overflow:hidden}
.abs{position:absolute}

/* sidebar */
.sidebar{position:absolute;left:0;top:0;width:84px;height:100%;background:var(--coral)}
.nav-btn{position:absolute;left:16px;width:52px;height:52px;border-radius:50%;background:var(--coral-strong);display:flex;align-items:center;justify-content:center}
.nav-btn.active{background:var(--white)}
.nav-btn svg{width:26px;height:26px}

/* sections */
.track{position:absolute;left:84px;top:0;width:931px;height:336px;background:var(--cream)}
.section-title{position:absolute;left:152px;font-size:19px;font-weight:700;letter-spacing:.2px}
.card{position:absolute;border:2px solid var(--coral);border-radius:8px;background:var(--white);overflow:hidden}
.select{position:absolute;top:14px;height:32px;width:148px;border:1px solid #e6e6e6;border-radius:8px;font-size:8px;font-weight:600;padding:10px 10px;background:#fff}
.select svg{position:absolute;right:10px;top:10px}
.entry-list{position:absolute;left:14px;top:60px;width:307px;background:#fff6f6;border-radius:6px;padding:4px 10px}
.entry-list li{list-style:none;display:flex;font-size:7px;color:#777;height:16px;align-items:center;border-bottom:1px solid #fbe9e9}
.entry-list li:last-child{border:none}
.entry-list .num{width:18px}.entry-list .who{width:112px}
.note{position:absolute;left:14px;top:136px;width:307px;height:62px;border:1px solid #e6e6e6;border-radius:8px;font-size:8px;font-weight:600;padding:11px 10px}

.cal-head{position:absolute;left:0;top:0;width:100%;height:66px;background:var(--coral);color:#fff;text-align:center}
.cal-head .day{font-size:24px;font-weight:600;margin-top:10px;line-height:1}
.cal-head .month{font-size:12px;font-weight:500;margin-top:2px}
.cal-head svg{position:absolute;top:18px}
.cal-grid{position:absolute;left:14px;top:76px;width:180px;display:grid;grid-template-columns:repeat(7,1fr);row-gap:0}
.cal-grid span{height:21.2px;font-size:7px;font-weight:600;display:flex;align-items:center;justify-content:center}
.cal-grid .out{color:#ccc;font-weight:400}
.cal-grid .today{color:#fff}
.cal-grid .today i{font-style:normal;width:15px;height:15px;border-radius:50%;background:var(--coral);display:flex;align-items:center;justify-content:center}

.pick{position:absolute;width:36px;height:34px;border:1px solid #eee;border-radius:10px;font-size:10px;font-weight:500;display:flex;align-items:center;justify-content:center;background:#fff;box-shadow:0 2px 4px rgba(0,0,0,.05)}
.pick.on{background:var(--coral);color:#fff;border-color:var(--coral)}
.minutes-band{position:absolute;left:0;top:111px;width:100%;height:54px;background:#fff}
.hours-band{position:absolute;left:0;top:0;width:100%;height:111px;background:#fff}
.duration{position:absolute;left:0;bottom:0;width:100%;height:50px;background:var(--coral);color:#fff;font-size:18px;font-weight:600;display:flex;align-items:center;justify-content:center;letter-spacing:.5px}

.ghost-btn{position:absolute;border:1.5px dashed var(--coral);border-radius:10px;color:var(--coral-strong);font-size:12px;font-weight:500;display:flex;align-items:center;justify-content:center;gap:6px;background:transparent}

/* statistics */
.stat-band{position:absolute;left:84px;top:412px;width:931px;height:170px;background:linear-gradient(100deg,#ff9a5a 0%,#ff8660 40%,#ff7a6a 70%,#ff6e6c 100%)}
.stat-card{position:absolute;top:392px;width:389px;height:216px;background:var(--panel);border-radius:6px;overflow:hidden;box-shadow:0 6px 10px rgba(255,110,108,.25)}
.stat-head{position:absolute;top:0;height:41px;display:flex;align-items:center;font-size:11.5px;font-weight:500}
.legend{position:absolute;list-style:none;color:#eee;font-size:7.5px}
.legend li{display:flex;align-items:center;height:19px}
.legend .dot{width:5px;height:5px;border-radius:50%;margin-right:5px}
.legend .h{width:43px}.legend .c{width:56px}.legend .p{font-weight:700}

/* tasks */
.day-band{position:absolute;left:84px;width:931px;height:29px;background:var(--cream);color:var(--orange);font-size:11.5px;font-weight:500;display:flex;align-items:center;padding:0 68px}
.day-band .date{margin-left:11px}
.day-band .total{margin-left:auto}
.task{position:absolute;left:152px;width:795px;height:91px;background:#fff;border-radius:6px;box-shadow:0 2px 6px rgba(0,0,0,.06);overflow:hidden}
.task-top{height:26px;background:var(--row);display:flex;align-items:center;padding:0 15px;font-size:7.5px;font-weight:600}
.task-top .dot{width:8px;height:8px;border-radius:50%;margin-right:5px}
.task-top .actions{margin-left:auto;margin-right:20px;color:#aaa;font-weight:400;text-decoration:underline;word-spacing:8px}
.task-main{position:absolute;left:15px;top:36px;width:640px;font-size:11.5px;font-weight:500;display:flex;border-bottom:1px solid var(--line);padding-bottom:8px}
.task-main .person{width:163px}
.task-desc{position:absolute;left:15px;top:68px;font-size:8px;color:#555}
.task-time{position:absolute;right:0;top:26px;width:127px;height:65px;background:var(--row);text-align:center}
.task-time .len{font-size:18px;font-weight:500;margin-top:12px;display:flex;align-items:center;justify-content:center;gap:4px}
.task-time .len i{width:8px;height:8px;border-radius:50%;background:#bbb;display:inline-block}
.task-time .span{font-size:5.5px;margin-top:5px}
.task.hot{border:1.5px solid var(--coral)}
.task.hot .task-top{background:var(--coral-soft)}
.task.hot .task-main{color:var(--coral)}
.task.hot .task-time{background:var(--coral);color:#fff}
.task.hot .task-time .len i{background:#fff}
</style>
</head>
<body>
<main class="dashboard">

  <nav class="sidebar" aria-label="Main navigation">
    <div class="nav-btn active" style="top:32px"><svg viewBox="0 0 26 26"><circle cx="13" cy="13" r="11" fill="#ff6e6c"/><path d="M13 7v6l3 3" stroke="#fff" stroke-width="2.4" fill="none" stroke-linecap="round"/></svg></div>
    <div class="nav-btn" style="top:96px"><svg viewBox="0 0 26 26"><path d="M12 3a10 10 0 1 0 10 11H12z" fill="#fff"/><path d="M14 2v10h10A10 10 0 0 0 14 2z" fill="#fff"/></svg></div>
    <div class="nav-btn" style="top:159px"><svg viewBox="0 0 26 26"><rect x="3" y="3" width="20" height="20" rx="5" fill="#fff"/><path d="M7 10l2 2 3-3M7 17l2 2 3-3" stroke="#ff6e6c" stroke-width="1.8" fill="none"/><path d="M14 11h5M14 17h5" stroke="#ff6e6c" stroke-width="1.8"/></svg></div>
    <div class="nav-btn" style="top:222px"><svg viewBox="0 0 26 26"><circle cx="13" cy="8" r="5" fill="#fff"/><path d="M4 24c0-6 4-9 9-9s9 3 9 9z" fill="#fff"/></svg></div>
    <div class="nav-btn" style="top:1365px"><svg viewBox="0 0 26 26"><circle cx="13" cy="13" r="8" fill="none" stroke="#fff" stroke-width="6" stroke-dasharray="3.4 1.8"/><circle cx="13" cy="13" r="7" fill="none" stroke="#fff" stroke-width="4"/></svg></div>
    <div class="nav-btn" style="top:1431px"><svg viewBox="0 0 26 26"><path d="M5 3h9v20H5a2 2 0 0 1-2-2V5a2 2 0 0 1 2-2z" fill="#fff"/><path d="M14 13h9M19 9l4 4-4 4" stroke="#fff" stroke-width="2.2" fill="none"/></svg></div>
  </nav>

  <!-- Track your time -->
  <section class="track"></section>
  <h2 class="section-title" style="top:33px">TRACK YOUR TIME</h2>

  <div class="card entry-card" style="left:152px;top:66px;width:340px;height:217px">
    <div class="select" style="left:14px">Select Project<svg width="14" height="8" viewBox="0 0 14 8"><path d="M1 1l6 6 6-6" stroke="#999" fill="none"/></svg></div>
    <div class="select" style="left:174px">Select Type<svg width="14" height="8" viewBox="0 0 14 8"><path d="M1 1l6 6 6-6" stroke="#999" fill="none"/></svg></div>
    <ul class="entry-list">
      <li><span class="num">1.</span><span class="who">Mara Lindqvist</span>Progect 1</li>
      <li><span class="num">2.</span><span class="who">Owen Castell</span>Progect 2</li>
      <li><span class="num">3.</span><span class="who">Priya Halden</span>Progect 3</li>
      <li><span class="num">4.</span><span class="who">Noel Brandt</span>Progect 4</li>
    </ul>
    <div class="note">What did you do?</div>
  </div>

  <div class="card calendar" style="left:509px;top:66px;width:210px;height:217px">
    <div class="cal-head">
      <svg style="left:22px" width="14" height="28" viewBox="0 0 14 28"><path d="M12 2L2 14l10 12" stroke="#fff" stroke-width="2" fill="none"/></svg>
      <div class="day">28</div><div class="month">October</div>
      <svg style="right:22px" width="14" height="28" viewBox="0 0 14 28"><path d="M2 2l10 12L2 26" stroke="#fff" stroke-width="2" fill="none"/></svg>
    </div>
    <div class="cal-grid">
      <span class="out">25</span><span class="out">26</span><span class="out">27</span><span class="out">28</span><span class="out">29</span><span class="out">30</span><span>1</span>
      <span>2</span><span>3</span><span>4</span><span>5</span><span>6</span><span>7</span><span>8</span>
      <span>9</span><span>10</span><span>11</span><span>12</span><span>13</span><span>14</span><span>15</span>
      <span>16</span><span>17</span><span>18</span><span>19</span><span>20</span><span>21</span><span>22</span>
      <span>23</span><span>24</span><span>25</span><span>26</span><span>27</span><span class="today"><i>28</i></span><span>29</span>
      <span>30</span><span>31</span><span class="out">1</span><span class="out">2</span><span class="out">3</span><span class="out">4</span><span class="out">5</span>
    </div>
  </div>

  <div class="card duration-card" style="left:736px;top:66px;width:211px;height:217px;background:var(--cream)">
    <div class="hours-band"></div>
    <div class="pick" style="left:14px;top:15px">1 h</div>
    <div class="pick on" style="left:62px;top:15px">2 h</div>
    <div class="pick" style="left:110px;top:15px">3 h</div>
    <div class="pick" style="left:157px;top:15px">4 h</div>
    <div class="pick" style="left:14px;top:63px">5 h</div>
    <div class="pick" style="left:62px;top:63px">6 h</div>
    <div class="pick" style="left:110px;top:63px">7 h</div>
    <div class="pick" style="left:157px;top:63px">8 h</div>
    <div class="minutes-band"></div>
    <div class="pick" style="left:14px;top:122px">0 m</div>
    <div class="pick" style="left:62px;top:122px">15 m</div>
    <div class="pick on" style="left:110px;top:122px">30 m</div>
    <div class="pick" style="left:157px;top:122px">45 m</div>
    <div class="duration">2 h 30 m</div>
  </div>

  <button class="ghost-btn" style="left:497px;top:293px;width:106px;height:32px">
    <svg width="9" height="10" viewBox="0 0 9 10"><path d="M0 0h7l2 2v8H0z" fill="#ff6e6c"/><rect x="2" y="1" width="4" height="3" fill="#fff"/></svg>Save
  </button>

  <!-- Statistics -->
  <h2 class="section-title" style="top:353px">STATISTICS</h2>
  <div class="stat-band"></div>

  <article class="stat-card" style="left:152px">
    <div class="stat-head" style="left:16px;color:var(--orange)">CURRENT MONTH</div>
    <div class="stat-head" style="left:230px;width:159px;background:var(--orange);color:var(--ink);justify-content:flex-end;padding-right:16px;font-weight:600">Total: 50:45 h</div>
    <svg class="abs" style="left:30px;top:50px" width="150" height="150" viewBox="0 0 150 150" role="img" aria-label="Donut chart: Customer A 89%, Customer B 11%">
      <circle cx="72" cy="75" r="49" fill="none" stroke="#ff8a85" stroke-width="42" stroke-dasharray="274 34" transform="rotate(-8 72 75)"/>
      <path d="M108 48 L128 30 Q142 40 142 70 L108 70 Q104 58 108 48z" fill="#f9a94b"/>
    </svg>
    <ul class="legend" style="left:234px;top:74px">
      <li><i class="dot" style="background:var(--coral)"></i><span class="h">40:45 h</span><span class="c">Customer A</span><span class="p">(89%)</span></li>
      <li><i class="dot" style="background:var(--orange)"></i><span class="h">10:00 h</span><span class="c">Customer B</span><span class="p">(11%)</span></li>
    </ul>
  </article>

  <article class="stat-card" style="left:558px">
    <div class="stat-head" style="left:0;width:231px;padding-left:16px;color:#fff">SEPTEMBER</div>
    <div class="stat-head" style="left:231px;width:158px;background:var(--panel-head);color:#fff;justify-content:flex-end;padding-right:16px;font-weight:600">Gesamt: 114:00 h</div>
    <svg class="abs" style="left:20px;top:60px" width="170" height="130" viewBox="0 0 170 130" role="img" aria-label="Bar chart of hours per customer">
      <rect x="2" y="27" width="22" height="110" rx="11" fill="#ff8a85"/>
      <rect x="30" y="3" width="22" height="134" rx="11" fill="#f9a94b"/>
      <rect x="58" y="39" width="22" height="98" rx="11" fill="#6ee35c"/>
      <rect x="86" y="62" width="22" height="75" rx="11" fill="#8fd1f7"/>
      <rect x="114" y="27" width="22" height="110" rx="11" fill="#ffc9cf"/>
      <rect x="142" y="43" width="22" height="94" rx="11" fill="#f7e44a"/>
      <rect x="0" y="126" width="170" height="10" fill="#3a3335"/>
    </svg>
    <ul class="legend" style="left:233px;top:73px">
      <li><i class="dot" style="background:var(--coral)"></i><span class="h">40:45 h</span><span class="c">Customer A</span><span class="p">(53%)</span></li>
      <li><i class="dot" style="background:var(--orange)"></i><span class="h">08:15 h</span><span class="c">Customer B</span><span class="p">(13%)</span></li>
      <li><i class="dot" style="background:var(--green)"></i><span class="h">20:00 h</span><span class="c">Customer C</span><span class="p">(34%)</span></li>
      <li><i class="dot" style="background:var(--blue)"></i><span class="h">22:45 h</span><span class="c">Customer D</span><span class="p">(53%)</span></li>
      <li><i class="dot" style="background:var(--pink)"></i><span class="h">02:15 h</span><span class="c">Customer E</span><span class="p">(13%)</span></li>
      <li><i class="dot" style="background:var(--yellow)"></i><span class="h">20:00 h</span><span class="c">Customer F</span><span class="p">(34%)</span></li>
    </ul>
  </article>

  <button class="ghost-btn" style="left:497px;top:624px;width:106px;height:28px">Show all</button>

  <!-- Tasks -->
  <h2 class="section-title" style="top:697px">YOUR TASKS</h2>
  <button class="ghost-btn" style="left:838px;top:688px;width:106px;height:28px">
    <svg width="11" height="9" viewBox="0 0 11 9"><path d="M0 1.5h11M0 4.5h11M0 7.5h11" stroke="#ff6e6c"/><circle cx="7" cy="1.5" r="1.3" fill="#fff" stroke="#ff6e6c"/><circle cx="3" cy="4.5" r="1.3" fill="#fff" stroke="#ff6e6c"/><circle cx="6" cy="7.5" r="1.3" fill="#fff" stroke="#ff6e6c"/></svg>Filter
  </button>

  <div class="day-band" style="top:728px"><span>WEDNESDAY</span><span class="date">December 9th</span><span class="total">7H 30M</span></div>
  <article class="task" style="top:764px">
    <div class="task-top"><i class="dot" style="background:var(--coral)"></i>Coding<span class="actions">Delete Edit</span></div>
    <div class="task-main"><span class="person">Mara Lindqvist</span>Project 1</div>
    <p class="task-desc">Some description what the user did on that project</p>
    <div class="task-time"><div class="len"><i></i>4h 30m</div><div class="span">09.00 a.m. - 14.30 p.m.</div></div>
  </article>

  <div class="day-band" style="top:865px"><span>TUESDAY</span><span class="date">December 8th</span><span class="total">7H 30M</span></div>
  <article class="task hot" style="top:900px">
    <div class="task-top"><i class="dot" style="background:var(--green)"></i>Meeting<span class="actions">Delete Edit</span></div>
    <div class="task-main"><span class="person">Owen Castell</span>Project 1</div>
    <p class="task-desc">Some description what the user did on that project</p>
    <div class="task-time"><div class="len"><i></i>4h 30m</div><div class="span">09.00 a.m. - 14.30 p.m.</div></div>
  </article>
  <article class="task" style="top:1008px">
    <div class="task-top"><i class="dot" style="background:var(--blue)"></i>Project Management<span class="actions">Delete Edit</span></div>
    <div class="task-main"><span class="person">Priya Halden</span>Project 1</div>
    <p class="task-desc">Some description what the user did on that project</p>
    <div class="task-time"><div class="len"><i></i>4h 30m</div><div class="span">09.00 a.m. - 14.30 p.m.</div></div>
  </article>
  <article class="task" style="top:1116px">
    <div class="task-top"><i class="dot" style="background:var(--coral)"></i>Coding<span class="actions">Delete Edit</span></div>
    <div class="task-main"><span class="person">Mara Lindqvist</span>Project 1</div>
    <p class="task-desc">Some description what the user did on that project</p>
    <div class="task-time"><div class="len"><i></i>4h 30m</div><div class="span">09.00 a.m. - 14.30 p.m.</div></div>
  </article>

  <div class="day-band" style="top:1217px"><span>MONDAY</span><span class="date">December 7th</span><span class="total">7H 30M</span></div>
  <article class="task" style="top:1252px">
    <div class="task-top"><i class="dot" style="background:var(--green)"></i>Meeting<span class="actions">Delete Edit</span></div>
    <div class="task-main"><span class="person">Owen Castell</span>Project 1</div>
    <p class="task-desc">Some description what the user did on that project</p>
    <div class="task-time"><div class="len"><i></i>4h 30m</div><div class="span">09.00 a.m. - 14.30 p.m.</div></div>
  </article>
  <article class="task" style="top:1360px">
    <div class="task-top"><i class="dot" style="background:var(--blue)"></i>Project Management<span class="actions">Delete Edit</span></div>
    <div class="task-main"><span class="person">Priya Halden</span>Project 1</div>
    <p class="task-desc">Some description what the user did on that project</p>
    <div class="task-time"><div class="len"><i></i>4h 30m</div><div class="span">09.00 a.m. - 14.30 p.m.</div></div>
  </article>

  <button class="ghost-btn" style="left:497px;top:1467px;width:106px;height:28px">Show all</button>
</main>
</body>
</html>
```